Office & Van Signage

We are looking for a graphic designer to use our new logo and create appropriate signage to replace existing on our van and at the office.

```html
<!DOCTYPE html>
<html lang="en">
<head>
<meta charset="utf-8">
<title>Crafted Haven – Office Signage</title>
<link href="https://fonts.googleapis.com/css2?family=Poppins:wght@300;400;600;700&display=swap" rel="stylesheet">
<style>
  :root{
    --ink:#111111;
    --paper:#ffffff;
    --backdrop:#efefed;
    --fascia:#c9c4bb;
    --rule:#8a8a8a;
    --soft:#9a9a9a;
  }
  *{box-sizing:border-box;margin:0;padding:0}
  html,body{width:1200px;height:1200px;overflow:hidden}
  body{background:var(--backdrop);font-family:'Poppins',sans-serif;color:var(--ink);position:relative}

  .fascia{position:absolute;left:200px;top:70px;width:800px;height:120px;background:var(--fascia);display:flex;align-items:center;justify-content:center}
  .fascia-plate{background:var(--paper);width:420px;height:100px;display:flex;flex-direction:column;align-items:center;justify-content:center}
  .brand-name{font-weight:300;letter-spacing:.28em;text-transform:uppercase;text-align:center}
  .brand-tag{font-weight:400;letter-spacing:.18em;text-transform:uppercase;margin-top:6px;text-align:center}
  .fascia .brand-name{font-size:26px}
  .fascia .brand-tag{font-size:10px}
  .brand-rule{width:80%;height:1px;background:var(--ink);margin-top:6px}

  .windows{position:absolute;left:140px;top:240px;display:flex;gap:40px}
  .panel{width:280px;height:400px;background:var(--paper);display:flex;flex-direction:column;box-shadow:0 2px 8px rgba(0,0,0,.12)}

  .hours-top{flex:0 0 190px;padding:34px 22px 0;line-height:1.15}
  .hours-top .light{font-weight:300;font-size:26px;text-transform:uppercase}
  .hours-top .bold{font-weight:700;font-size:28px;text-transform:uppercase}
  .hours-bottom{flex:1;background:var(--ink);color:var(--paper);text-align:center;padding-top:30px;line-height:1.25}
  .hours-bottom .label{font-weight:700;font-size:24px}
  .hours-bottom .days{font-weight:400;font-size:21px}
  .hours-bottom .time{font-weight:700;font-size:27px}
  .hours-bottom .note{font-weight:400;font-size:19px}

  .panel-mark{align-items:center;justify-content:center}
  .panel-mark .brand-name{font-size:21px;color:var(--soft)}
  .panel-mark .brand-tag{font-size:8px;color:var(--soft)}
  .panel-mark .brand-rule{background:var(--soft);width:210px}

  .contact-top{flex:0 0 200px;background:var(--ink);color:var(--paper);display:flex;flex-direction:column;align-items:center;justify-content:center}
  .contact-top .brand-name{font-size:20px}
  .contact-top .brand-tag{font-size:8px}
  .contact-top .brand-rule{background:var(--paper);width:210px}
  .contact-list{flex:1;padding:18px 20px 0}
  .contact-list li{list-style:none;border-bottom:1px solid var(--rule);padding:12px 0 8px;text-align:center}
  .contact-list li:last-child{border-bottom:none}
  .contact-web{font-size:18px}
  .contact-phone{font-size:22px;font-weight:300}
  .contact-mail{font-size:11px;font-weight:600;text-transform:uppercase}

  .door-panel{position:absolute;left:510px;top:690px;width:180px;height:460px;background:var(--ink);display:flex;flex-direction:column;box-shadow:0 2px 8px rgba(0,0,0,.12)}
  .door-brand{background:var(--paper);height:130px;display:flex;flex-direction:column;align-items:center;justify-content:center}
  .door-brand .brand-name{font-size:13px}
  .door-brand .brand-tag{font-size:5.5px}
  .door-brand .brand-rule{width:130px}
  .door-hours{color:var(--paper);text-align:center;padding:28px 0 20px;line-height:1.3}
  .door-hours .label{font-weight:700;font-size:14px}
  .door-hours .days{font-size:12px}
  .door-hours .time{font-weight:700;font-size:16px}
  .door-hours .note{font-size:11px}
  .door-contact{background:var(--paper);padding:6px 12px}
  .door-contact li{list-style:none;border-bottom:1px solid var(--rule);text-align:center;padding:8px 0 5px}
  .door-contact li:last-child{border-bottom:none}
  .door-contact .contact-web{font-size:11px}
  .door-contact .contact-phone{font-size:15px}
  .door-contact .contact-mail{font-size:7px}
  .door-social{flex:1;display:flex;align-items:center;justify-content:center;gap:10px}
  .social-dot{width:12px;height:12px;background:var(--paper)}
</style>
</head>
<body>

<header class="fascia">
  <div class="fascia-plate">
    <div class="brand-name">Crafted Haven</div>
    <div class="brand-rule"></div>
    <div class="brand-tag">Kitchens | Bathrooms | Interiors</div>
  </div>
</header>

<section class="windows">
  <article class="panel panel-hours">
    <div class="hours-top">
      <div class="light">Selections</div>
      <div class="light">Studio &amp;</div>
      <div class="bold">Showroom</div>
    </div>
    <div class="hours-bottom">
      <div class="label">OPENING HOURS</div>
      <div class="days">MONDAY - FRIDAY</div>
      <div class="time">9am - 5pm</div>
      <div class="note">or By Appointment</div>
    </div>
  </article>

  <article class="panel panel-mark">
    <div class="brand-name">Crafted Haven</div>
    <div class="brand-rule"></div>
    <div class="brand-tag">Kitchens | Bathrooms | Interiors</div>
  </article>

  <article class="panel panel-contact">
    <div class="contact-top">
      <div class="brand-name">Crafted Haven</div>
      <div class="brand-rule"></div>
      <div class="brand-tag">Kitchens | Bathrooms | Interiors</div>
    </div>
    <ul class="contact-list">
      <li class="contact-web">CRAFTEDHAVEN.COM.AU</li>
      <li class="contact-phone">(02) 5550 1842</li>
      <li class="contact-mail">office@craftedhaven.com.au</li>
    </ul>
  </article>
</section>

<aside class="door-panel">
  <div class="door-brand">
    <div class="brand-name">Crafted Haven</div>
    <div class="brand-rule"></div>
    <div class="brand-tag">Kitchens | Bathrooms | Interiors</div>
  </div>
  <div class="door-hours">
    <div class="label">OPENING HOURS</div>
    <div class="days">MONDAY - FRIDAY</div>
    <div class="time">9am - 5pm</div>
    <div class="note">or By Appointment</div>
  </div>
  <ul class="door-contact">
    <li class="contact-web">CRAFTEDHAVEN.COM.AU</li>
    <li class="contact-phone">(02) 5550 1842</li>
    <li class="contact-mail">office@craftedhaven.com.au</li>
  </ul>
  <div class="door-social">
    <span class="social-dot"></span>
    <span class="social-dot"></span>
  </div>
</aside>

</body>
</html>
```